Stationary w/Bizz Card for Medical Equipment Company
Harborline Biomedical Systems
Stationary w/Bizz Card  for Medical Equipment Company - Health
Creative Brief
Professional
Derek Palmer
Vice President
415 Wexmoor Avenue Jacksonville, FL 32209
derek.palmer@hb-sysmed.net
www.hb-sysmed.net
Somewhere on the business card please put "Harborline Biomedical Systems"

```html
<!DOCTYPE html>
<html lang="en">
<head>
<meta charset="utf-8">
<title>Harborline Biomedical Systems – Business Card</title>
<link href="https://fonts.googleapis.com/css2?family=Arimo:ital,wght@0,400;0,700;1,700&display=swap" rel="stylesheet">
<style>
  :root {
    --stage: #e9e9e9;
    --card-white: #ffffff;
    --brand-blue: #1b8fd6;
    --deep-blue: #0d6fb8;
    --text-dark: #3a3a3a;
    --silver-light: #d4d4d4;
    --silver-dark: #7d7d7d;
    --wave-grey: #c9ced3;
  }
  * { margin: 0; padding: 0; box-sizing: border-box; }
  html, body { width: 1200px; height: 402px; overflow: hidden; }
  body {
    background: var(--stage);
    font-family: "Arimo", Arial, sans-serif;
    position: relative;
  }
  .card {
    position: absolute;
    top: 66px;
    width: 566px;
    height: 278px;
    overflow: hidden;
    box-shadow: 0 3px 8px rgba(0,0,0,.25);
  }
  .card-front { left: 22px; background: var(--card-white); }
  .card-back {
    left: 612px;
    background: linear-gradient(135deg, var(--silver-light) 0%, #a8a8a8 45%, var(--silver-dark) 100%);
  }

  /* Front */
  .brand-lockup {
    position: absolute; left: 40px; top: 62px;
    display: flex; align-items: center; gap: 12px;
  }
  .brand-dot { width: 22px; height: 22px; border-radius: 50%; background: var(--brand-blue); }
  .brand-name { font-size: 50px; font-weight: 700; color: var(--brand-blue); letter-spacing: 1px; }

  .contact-block { position: absolute; left: 412px; top: 34px; }
  .person-name { font-size: 19px; font-weight: 700; color: var(--brand-blue); }
  .person-title { font-size: 13px; color: var(--text-dark); margin-top: 2px; }
  .contact-list { list-style: none; margin-top: 16px; }
  .contact-list li {
    display: flex; align-items: center; gap: 6px;
    font-size: 12px; color: var(--text-dark); line-height: 17.5px;
  }
  .contact-icon { width: 11px; height: 11px; flex: none; }

  .wave-band { position: absolute; left: 0; bottom: 0; width: 566px; height: 110px; }
  .address {
    position: absolute; right: 40px; bottom: 18px;
    font-size: 12px; color: #fff;
  }

  /* Back */
  .back-lockup {
    position: absolute; left: 0; right: 0; top: 70px;
    display: flex; justify-content: center; align-items: center; gap: 16px;
  }
  .back-dot { width: 30px; height: 30px; border-radius: 50%; background: #fff; }
  .back-name { font-size: 76px; font-weight: 700; color: #fff; letter-spacing: 2px; }
  .tagline {
    position: absolute; right: 34px; top: 214px;
    font-size: 20px; font-weight: 700; font-style: italic; color: #fff;
  }
</style>
</head>
<body>
  <section class="card card-front">
    <div class="brand-lockup">
      <span class="brand-dot"></span>
      <span class="brand-name">halvorn</span>
    </div>

    <div class="contact-block">
      <p class="person-name">Derek Palmer</p>
      <p class="person-title">Vice President</p>
      <ul class="contact-list">
        <li><svg class="contact-icon" viewBox="0 0 12 12"><circle cx="6" cy="6" r="6" fill="#1b8fd6"/><path d="M4 3.2l1.2 1.4-.6.8c.4.9 1 1.5 1.9 1.9l.8-.6 1.4 1.2-.7 1c-2.6-.4-4.6-2.4-5-5z" fill="#fff"/></svg>800-555-0142</li>
        <li><svg class="contact-icon" viewBox="0 0 12 12"><circle cx="6" cy="6" r="6" fill="#1b8fd6"/><rect x="4" y="2.5" width="4" height="7" rx=".8" fill="#fff"/></svg>904-555-0187</li>
        <li><svg class="contact-icon" viewBox="0 0 12 12"><circle cx="6" cy="6" r="6" fill="#1b8fd6"/><rect x="3" y="4" width="6" height="4.5" fill="#fff"/><rect x="4" y="2.5" width="4" height="1.5" fill="#fff"/></svg>904-555-0123</li>
        <li><svg class="contact-icon" viewBox="0 0 12 12"><circle cx="6" cy="6" r="6" fill="#1b8fd6"/><rect x="3" y="4" width="6" height="4" fill="#fff"/><path d="M3 4l3 2.2L9 4" stroke="#1b8fd6" stroke-width=".7" fill="none"/></svg>derek.palmer@hb-sysmed.net</li>
        <li><svg class="contact-icon" viewBox="0 0 12 12"><circle cx="6" cy="6" r="6" fill="#1b8fd6"/><circle cx="6" cy="6" r="3" fill="none" stroke="#fff" stroke-width=".8"/><path d="M3 6h6M6 3v6" stroke="#fff" stroke-width=".6"/></svg>www.hb-sysmed.net</li>
      </ul>
    </div>

    <svg class="wave-band" viewBox="0 0 566 110" preserveAspectRatio="none">
      <defs>
        <linearGradient id="bandBlue" x1="0" y1="0" x2="1" y2="0">
          <stop offset="0" stop-color="#5bb6ea"/>
          <stop offset="1" stop-color="#0d6fb8"/>
        </linearGradient>
      </defs>
      <path d="M0 18 C150 70 330 0 566 30 L566 110 L0 110Z" fill="var(--wave-grey)"/>
      <path d="M0 34 C160 80 340 12 566 42 L566 110 L0 110Z" fill="#e4e7ea"/>
      <path d="M0 48 C170 92 350 26 566 56 L566 110 L0 110Z" fill="url(#bandBlue)"/>
    </svg>
    <p class="address">415 Wexmoor Avenue Jacksonville, FL 32209</p>
  </section>

  <section class="card card-back">
    <div class="back-lockup">
      <span class="back-dot"></span>
      <span class="back-name">halvorn</span>
    </div>
    <p class="tagline">Harborline Biomedical Systems</p>
  </section>
</body>
</html>
```